Webdesign  Seminare im Bereich persönliche Entwicklung, Spiritualität und Coaching
Webdesign Seminare im Bereich persönliche Entwicklung, Spiritualität und Coaching
Zielgruppe
Wir bieten Seminare im Bereich persönliche Entwicklung, Spiritualität und Coaching an. Unsere Zielgruppe umfasst Menschen zw. 18 und 75 jeglichen Berufsstandes, die sich dafür interessieren ihre tieferen innewohnenden Potenziale kennenzulernen und zu eröffnen.
Dieser Auftrag hier ist ein Teaser-Projekt. Wir wachsen konstant, möchten mehrere Folgeaufträge vergeben und suchen auf diesem Weg einen langfristigen Partner.
Aufgabenstellung
- keine esoterischen Klischee-Bilder, nichts Verspieltes
- unser Auftritt (hier vorerst die Website) soll wärmer wirken als dies aktuell der Fall ist, die Klarheit darf dabei jedoch nicht verloren gehen
- klar, warm, offen, vertraut, seriös
- das Logo darf verändert werden
Aktuell ist recht wenig Bildmaterial vorhanden. Hier wird demnächst nachproduziert. Bitte vorerst, wenn designtechnisch angebracht, Stockmaterial (als Platzhalter) verwenden.

```html
<!DOCTYPE html>
<html lang="de">
<head>
<meta charset="utf-8">
<title>Basisworkshops – Julius Brandt</title>
<link rel="stylesheet" href="https://fonts.googleapis.com/css2?family=Lato:ital,wght@0,400;0,700;1,400;1,700&family=Montserrat:wght@400;500&display=swap">
<style>
:root{
  --bg:#edebe6;
  --white:#ffffff;
  --yellow:#fdd06b;
  --yellow-soft:#fdf3de;
  --brown:#4a3a14;
  --text:#585858;
  --ink:#2d2d2d;
  --line:#e6e3dd;
  --rule:#9a9893;
}
*{box-sizing:border-box;margin:0;padding:0}
html,body{width:760px;height:1200px;overflow:hidden}
body{background:var(--bg);font-family:"Lato",sans-serif;color:var(--text);position:relative}
a{color:inherit}

.site-header{position:absolute;left:0;top:0;width:760px;height:55px;background:var(--white)}
.brand{position:absolute;left:79px;top:17px;display:flex;align-items:center;gap:6px;font-family:"Lato",sans-serif;font-weight:700;font-size:15px;color:var(--brown)}
.brand-mark{width:10px;height:10px;background:var(--yellow)}
.main-nav{position:absolute;right:76px;top:22px;display:flex;gap:21px;font-family:"Montserrat",sans-serif;font-size:8px;color:var(--ink)}
.main-nav a{text-decoration:none;position:relative}
.main-nav a.active::after{content:"";position:absolute;left:-4px;right:-3px;top:13px;height:2px;background:var(--yellow)}

.hero{position:absolute;left:0;top:55px;width:760px;height:128px;
  background:linear-gradient(100deg,#6ea3cc 0%,#a9c6dc 30%,#d9dde0 55%,#efe2c8 78%,#f6e7a4 100%);
  display:flex;align-items:center;justify-content:center}
.hero h1{font-family:"Montserrat",sans-serif;font-weight:500;font-size:16px;letter-spacing:1.3px;color:var(--brown)}

.sub-nav{position:absolute;left:127px;top:219px;width:507px;height:21px;border-bottom:2px solid var(--yellow);display:flex;justify-content:space-between;padding:0 4px;font-size:8.5px;font-weight:400;color:var(--ink)}
.sub-nav a{text-decoration:none;position:relative;padding:0 4px}
.sub-nav a.active::after{content:"";position:absolute;left:0;right:0;bottom:-9px;height:2px;background:var(--brown)}

.dates{position:absolute;left:79px;top:263px;width:602px;height:370px;background:var(--white);border-radius:5px;overflow:hidden}
.dates table{width:100%;border-collapse:collapse;font-size:7.4px;line-height:12.5px;color:var(--text)}
.dates th{background:var(--yellow);height:34px;text-align:left;font-weight:700;font-size:8.5px;color:var(--brown)}
.dates td{border-bottom:1px solid var(--line);vertical-align:middle}
.dates .c-date{padding-left:24px;width:146px}
.dates .c-place{width:88px}
.dates .c-house{width:173px}
.dates .c-price{width:131px}
.dates tr.highlight td{background:var(--yellow-soft)}
.dates td a{text-decoration:underline;text-underline-offset:2px;text-decoration-thickness:.5px;color:#444}
.signup{display:inline-block;background:var(--yellow);color:var(--brown);font-size:7.4px;padding:3px 4px;text-decoration:none;font-family:"Montserrat",sans-serif}
.dates td a.signup{text-decoration:none;color:var(--brown)}
.notes{margin:15px 24px 0;border-left:2px solid var(--yellow);padding-left:8px;font-style:italic;font-size:6.6px;line-height:8px;color:#555}
.notes p{margin-bottom:15px}
.notes p.strong{font-weight:700;line-height:15.8px;margin-bottom:0;margin-top:-4px}

.divider{position:absolute;left:79px;top:661px;width:608px;height:1px;background:var(--rule)}

.intro{position:absolute;left:79px;top:681px;width:612px;font-size:8.5px;line-height:15.8px}
.intro p{margin-bottom:15.8px}

.times{position:absolute;left:241px;top:919px;width:278px;background:var(--white);border-radius:4px;overflow:hidden;font-size:7.4px}
.times h2{background:var(--yellow);height:34px;line-height:34px;padding-left:17px;font-size:8.5px;font-weight:700;color:var(--brown)}
.times .row{display:flex;justify-content:space-between;height:34px;align-items:center;padding:0 21px 0 17px;border-bottom:1px solid var(--line)}
.times .row:last-child{border-bottom:0}

.social{position:absolute;left:353px;top:1088px;display:flex;gap:9px}
.social span{width:12px;height:12px;border-radius:50%;background:var(--white);border:1px solid #d8d5ce}
.footer-nav{position:absolute;left:0;width:760px;top:1122px;display:flex;justify-content:center;gap:21px;font-family:"Montserrat",sans-serif;font-size:8px;color:var(--ink)}
.footer-nav a{text-decoration:none}
.footer-rule{position:absolute;left:62px;top:1156px;width:635px;height:1px;background:var(--rule)}
.copyright{position:absolute;left:0;width:760px;top:1174px;text-align:center;font-size:5.5px;color:#666}
</style>
</head>
<body>
<header class="site-header">
  <div class="brand"><span class="brand-mark"></span>Julius Brandt</div>
  <nav class="main-nav">
    <a href="#">Start</a><a href="#">Julius Brandt</a><a href="#">ResonanzFeld</a><a href="#" class="active">Termine</a><a href="#">Blog</a><a href="#">Kontakt</a>
  </nav>
</header>

<section class="hero" role="img" aria-label="Weicher Himmel mit Wolken im warmen Abendlicht">
  <h1>BASISWORKSHOPS</h1>
</section>

<nav class="sub-nav">
  <a href="#">Übersicht</a><a href="#" class="active">BasisWorkshop</a><a href="#">AufbauWorkshops</a><a href="#">OnlineErlebnisAbend</a><a href="#">LiveMeditationen</a><a href="#">Einzelsitzungen</a>
</nav>

<section class="dates">
  <table>
    <thead><tr><th class="c-date">Termin</th><th class="c-place">Ort</th><th class="c-house">Seminarhaus</th><th class="c-price">Preis</th><th></th></tr></thead>
    <tbody>
      <tr style="height:45px"><td class="c-date">16. – 20.01.2022</td><td>Edertal<br>(Kassel)</td><td>Seminarhaus Talblick<br><a href="#">www.seminarhaus-talblick.de</a></td><td>1.290,- €</td><td><a href="#" class="signup">Anmelden</a></td></tr>
      <tr style="height:38px"><td class="c-date">27. – 31.03.2022</td><td>Edertal<br>(Kassel)</td><td>Seminarhaus Talblick<br><a href="#">www.seminarhaus-talblick.de</a></td><td>1.290,- €</td><td><a href="#" class="signup">Anmelden</a></td></tr>
      <tr style="height:52px"><td class="c-date">25. – 29.04.2022</td><td>Kißlegg<br>(Bodensee)</td><td>Seminarhaus Morgenlicht<br><a href="#">www.seminarzentrum-<br>morgenlicht.de</a></td><td>1.390,- €**</td><td><a href="#" class="signup">Anmelden</a></td></tr>
      <tr class="highlight" style="height:40px"><td class="c-date">08. – 12.05.2022</td><td>Edertal<br>(Kassel)</td><td>Seminarhaus Talblick<br><a href="#">www.seminarhaus-talblick.de</a></td><td>1.290,- €</td><td><a href="#" class="signup">Anmelden</a></td></tr>
      <tr style="height:53px"><td class="c-date">16. – 20.05.2022</td><td>Franking<br>(Salzburg)</td><td>Seminarhaus Seewiese<br><a href="#">www.seminarhaus-seewiese</a></td><td>1.390,- €**</td><td><a href="#" class="signup">Anmelden</a></td></tr>
    </tbody>
  </table>
  <div class="notes">
    <p>Alle Preise inkl. gesetzlich gültiger Mehrwertsteuer, bei Präsenzveranstaltungen zuzüglich Unterkunft und Verpflegung, eine Ratenzahlung ist möglich nach Vereinbarung.</p>
    <p>** Der leicht erhöhte Preis ergibt sich aus den deutlich höheren Anreisekosten und -zeiten für unser Team (min. 9 Personen). Wir bitten um euer Verständnis.</p>
    <p class="strong">Das Seminarhaus lässt Maskenatteste leider nur ganz bedingt gelten. Mit einem Maskenattest musst du dir für die Wege im Seminarhaus und für das Bedienen am Buffet einen Faceshield mitbringen und aufsetzen.</p>
  </div>
</section>

<div class="divider"></div>

<section class="intro">
  <p>Im BasisWorkshop erlernst du den Zugang zum ResonanzFeld und wie du für dich und andere darin lesen und arbeiten kannst. Anhand unterschiedlicher Übungen erlangst du zum einen Sicherheit im Umgang mit dem Feld, zum anderen heilst du eine Vielzahl an Themen, die dich gerade in deinem Leben hinderlich beeinflussen.</p>
  <p>Nachdem zu Beginn des Workshops alle Teilnehmer ihren Zugang zum ResonanzFeld geöffnet haben, intensivieren wir die Verbindung durch unterschiedliche Lesungen, die in der Regel paarweise stattfinden und intensiv von mir und meinem Team von sehr erfahrenen Therapeuten begleitet werden. Hierbei betrachtest du unter anderem deine nächsten notwendigen Entwicklungsschritte und du reist mit Hilfe des ResonanzFeldes zu deinen tief abgespeicherten Blockaden und hemmenden Thematiken und löst diese zügig und nachhaltig auf.</p>
  <p>Übungen zur weiteren Öffnung deines Herzens und zur Erweiterung deiner Fähigkeit wahrhaft fühlen zu können, runden den Weg ab, den du während des Workshops beschreitest. Du wirst unterschiedliche kraftvolle Energien und Potenziale in dir öffnen und zum Ende des Workshops lässt du dir vom ResonanzFeld zeigen, welche praktischen Schritte in deinem Alltag notwendig sind, um diese dort vollständig zu etablieren.</p>
  <p>Weitere Informationen zum Lesen im ResonanzFeld findest du <a href="#">hier.</a></p>
</section>

<section class="times">
  <h2>Workshopzeiten</h2>
  <div class="row"><span>1. Tag</span><span>15.00 – 18.30 Uhr</span></div>
  <div class="row"><span>2. – 4. Tag</span><span>09.00 – 18.30 Uhr</span></div>
  <div class="row"><span>5. Tag</span><span>09.00 – 13.00 Uhr</span></div>
</section>

<div class="social" aria-label="Soziale Netzwerke"><span></span><span></span><span></span></div>
<nav class="footer-nav"><a href="#">Impressum</a><a href="#">Datenschutz</a><a href="#">AGB</a><a href="#">Kontakt</a></nav>
<div class="footer-rule"></div>
<p class="copyright">© 2022 All Rights Reserved</p>
</body>
</html>
```